Brisko Sky Park needs a new upscale business card design for our high end aircraft hangar complex

Brisko Sky Park (BSP) is a large, upscale jet hangar complex in the US housing expensive aircraft. We need a new business card design, using our current logo. We will be attending a industry convention and need a card design that will stand out and be remembered by aircraft owners and private pilots.

Target Market(s)

Aircraft pilots or owners looking for a new upscale hangar

Industry/Entity Type

Airport

Contact Information for Business Card

I like to use very heavy card stock, 400#, double sided. Square, no rounded edges please.

Colors
3276b5
0255a3
85abd2

Requirements
Must have
• An expensive, classy design, vivid colors.
Nice to have
• Needs to look very expensive and classy, and have some "pop". Designer must be able to download or copy my current typeface or fonts.
• One card side might be black with the "Logo and Brisko Sky Park Double line image in blue (or try gold, or glossy black), and perhaps have a grayed out "K480 jet silhouette". The other card side would have our contact info, and perhaps the "BSP Logo only". I'd like my contact info 'stacked', not in a paragraph format.
Should not have
• Should not look "too busy". Having a double-sided card will help.

```html
<!DOCTYPE html>
<html lang="en">
<head>
<meta charset="utf-8">
<title>Brisko Sky Park – Business Card</title>
<link href="https://fonts.googleapis.com/css2?family=Open+Sans:wght@400;600;700&display=swap" rel="stylesheet">
<style>
  :root {
    --backdrop: #000000;
    --card: #2e2f31;
    --text-main: #e2e2e2;
    --text-soft: #c8c8c8;
    --brand-blue: #3276b5;
    --brand-deep: #0255a3;
    --brand-light: #85abd2;
    --divider: rgba(133,171,210,0.35);
  }
  html, body {
    margin: 0;
    width: 1200px;
    height: 900px;
    overflow: hidden;
    background: var(--backdrop);
    font-family: "Open Sans", sans-serif;
  }
  .canvas { position: relative; width: 1200px; height: 900px; }
  .card {
    position: absolute;
    top: 271px;
    width: 456px;
    height: 281px;
    background: var(--card);
    border-radius: 0;
    overflow: hidden;
  }
  .card-front { left: 137px; }
  .card-back { left: 627px; }

  .brand-mark {
    position: absolute;
    margin: 0;
    line-height: 1;
    color: var(--brand-light);
    font-weight: 700;
  }
  .card-front .brand-mark {
    left: 40px; top: 100px; width: 184px;
    text-align: center;
    font-size: 68px;
    letter-spacing: 4px;
  }
  .divider {
    position: absolute;
    left: 237px; top: 80px;
    width: 1px; height: 120px;
    background: var(--divider);
  }
  .contact {
    position: absolute;
    left: 260px; top: 47px;
    color: var(--text-soft);
    font-size: 12.5px;
  }
  .contact .name {
    margin: 0;
    font-size: 18px;
    font-weight: 400;
    color: var(--text-main);
    line-height: 24px;
  }
  .contact .role { margin: 0 0 12px; line-height: 16px; color: var(--brand-light); }
  .contact .address { margin: 0 0 16px; line-height: 16px; font-style: normal; }
  .contact ul { list-style: none; margin: 0; padding: 0; }
  .contact li { display: flex; align-items: center; height: 19px; }
  .contact li svg { width: 10px; height: 10px; margin: 0 8px 0 1px; fill: var(--brand-light); }

  .back-lockup {
    position: absolute;
    left: 0; right: 0; top: 92px;
    text-align: center;
    color: var(--brand-light);
    font-weight: 700;
  }
  .back-lockup .brand-initials {
    margin: 0;
    font-size: 72px;
    letter-spacing: 5px;
    line-height: 72px;
  }
  .back-lockup .brand-name {
    margin: 2px 0 0;
    font-size: 27px;
    line-height: 30px;
    letter-spacing: 0.5px;
  }
</style>
</head>
<body>
<div class="canvas">
  <section class="card card-front">
    <p class="brand-mark">BSP</p>
    <div class="divider"></div>
    <div class="contact">
      <h1 class="name">Daniel Harper</h1>
      <p class="role">Managing Director</p>
      <address class="address">12345, Address Goes Here<br>Country Name, 123456.</address>
      <ul>
        <li><svg viewBox="0 0 10 10"><path d="M2 0.5 L3.6 2.6 L2.8 3.6 Q4 6 6.4 7.2 L7.4 6.4 L9.5 8 L8.4 9.5 Q3.5 9 0.5 1.6 Z"/></svg>(044)-456-7890</li>
        <li><svg viewBox="0 0 10 10"><rect x="2.5" y="0.5" width="5" height="3"/><rect x="0.5" y="3.5" width="9" height="4.5" rx="1"/><rect x="2.5" y="7" width="5" height="2.5"/></svg>123-456-7890</li>
        <li><svg viewBox="0 0 10 10"><path d="M0.5 2 H9.5 V8.5 H0.5 Z M1 2.4 L5 5.6 L9 2.4" stroke="#2e2f31" stroke-width="0.8"/></svg>info@briskoskypark.com</li>
        <li><svg viewBox="0 0 10 10"><circle cx="5" cy="5" r="4.6"/><path d="M0.6 5 H9.4 M5 0.4 V9.6 M5 0.6 Q2 5 5 9.4 M5 0.6 Q8 5 5 9.4" stroke="#2e2f31" stroke-width="0.6" fill="none"/></svg>www.briskoskypark.com</li>
      </ul>
    </div>
  </section>

  <section class="card card-back">
    <div class="back-lockup">
      <p class="brand-initials">BSP</p>
      <p class="brand-name">Brisko Sky Park</p>
    </div>
  </section>
</div>
</body>
</html>
```